Healthy Supplement featuring Moringa products

Need 3 business card options for our reps to order from Cardloom. Our reps will be ordering from Cardloom once we upload them. Attached is our current designs to show what info needs to be on the cards. Our website is www.tkvitality.com
The business cards will be a template for our reps to order from. Most of our reps are Asian & Hispanic. Please look at our website so you can see who we are to get the look and feel what we need.
Target Market(s)
Adults 30 on up. Health oriented people.
Industry/Entity Type
Health And Wellness
Contact Information for Business Card
Name
Title
Phone
Logo
www.tkvitality.com/my/username
Font styles to use
Requirements
Must have
- Please match our website look and colors. A moringa leaf is nice, but am open to something different.
Nice to have
- Healthy looking and warm, not super cold or too modern.
Should not have
- No harsh colors please.

```html
<!DOCTYPE html>
<html lang="en">
<head>
<meta charset="utf-8">
<title>TK Vitality Business Card</title>
<link rel="stylesheet" href="https://fonts.googleapis.com/css2?family=Montserrat:wght@800&family=Open+Sans:wght@400;600&display=swap">
<style>
  :root {
    --leaf: #62a60e;
    --leaf-light: #8cc21f;
    --orange: #ea6a1a;
    --ink: #111111;
    --paper: #ffffff;
    --backdrop: #ecebe7;
  }
  * { box-sizing: border-box; margin: 0; padding: 0; }
  html, body { width: 1200px; height: 900px; overflow: hidden; }
  body {
    background: var(--backdrop);
    font-family: "Open Sans", sans-serif;
    color: var(--ink);
    position: relative;
  }
  .card {
    position: absolute;
    left: 240px;
    width: 720px;
    height: 411px;
    overflow: hidden;
    box-shadow: 0 4px 14px rgba(0,0,0,.15);
  }
  .card--front { top: 28px; background: var(--paper); }
  .card--back { top: 463px; background: var(--leaf); }

  .rule { position: absolute; left: 62px; width: 340px; height: 3px; background: var(--orange); }
  .rule--top { top: 62px; }
  .rule--bottom { top: 150px; }

  .rep-name {
    position: absolute; left: 62px; top: 80px;
    font-family: "Montserrat", sans-serif; font-weight: 800; font-size: 28px;
    letter-spacing: .5px;
  }
  .rep-name__first { color: var(--orange); }
  .rep-title {
    position: absolute; left: 64px; top: 120px;
    font-size: 13px; font-weight: 600; color: var(--leaf); letter-spacing: .5px;
  }

  .contact-list { position: absolute; left: 62px; top: 172px; list-style: none; }
  .contact-item { display: flex; align-items: center; gap: 22px; height: 46px; font-size: 15px; line-height: 1.25; }
  .contact-icon { width: 30px; height: 30px; flex: none; }

  .brand {
    position: absolute; display: flex; align-items: center; gap: 14px;
    font-family: "Open Sans", sans-serif; font-weight: 600; white-space: nowrap;
  }
  .brand__dot { border-radius: 50%; flex: none; }
  .card--front .brand { left: 430px; top: 108px; font-size: 40px; color: var(--leaf); }
  .card--front .brand__dot { width: 34px; height: 34px; background: var(--leaf-light); }
  .card--back .brand { left: 50%; top: 150px; transform: translateX(-50%); font-size: 62px; color: var(--paper); }
  .card--back .brand__dot { width: 48px; height: 48px; background: var(--paper); }

  .edge-band { position: absolute; left: 0; bottom: 0; width: 720px; height: 30px; }

  .back-url {
    position: absolute; left: 0; right: 0; bottom: 42px; text-align: center;
    font-size: 20px; color: var(--ink);
  }
</style>
</head>
<body>

<section class="card card--front" aria-label="Card front">
  <div class="rule rule--top"></div>
  <h1 class="rep-name"><span class="rep-name__first">NAME</span> HERE</h1>
  <p class="rep-title">DESIGNATION</p>
  <div class="rule rule--bottom"></div>

  <ul class="contact-list">
    <li class="contact-item">
      <svg class="contact-icon" viewBox="0 0 30 30" aria-hidden="true"><circle cx="15" cy="15" r="15" fill="#111"/><path d="M15 7a5 5 0 0 0-5 5c0 4 5 9 5 9s5-5 5-9a5 5 0 0 0-5-5z" fill="#fff"/><circle cx="15" cy="12" r="1.8" fill="#111"/></svg>
      <span>48 Cedar Row STE B<br>Fairview, CA 90210</span>
    </li>
    <li class="contact-item">
      <svg class="contact-icon" viewBox="0 0 30 30" aria-hidden="true"><circle cx="15" cy="15" r="13.5" fill="#fff" stroke="#111" stroke-width="2"/><path d="M10 9l3-1 2 4-2 1.5c.8 2 2 3.2 3.5 3.8L18 15l4 2-1 3c-6 0-11-5-11-11z" fill="#111"/></svg>
      <span>Main: (555) 210-4410<br>Fax: (555) 210-4411</span>
    </li>
    <li class="contact-item">
      <svg class="contact-icon" viewBox="0 0 30 30" aria-hidden="true"><circle cx="15" cy="15" r="15" fill="#111"/><rect x="8" y="10" width="14" height="10" rx="1" fill="#fff"/><path d="M8.5 10.5l6.5 5 6.5-5" fill="none" stroke="#111" stroke-width="1.5"/></svg>
      <span>info@tkvitality.com</span>
    </li>
    <li class="contact-item">
      <svg class="contact-icon" viewBox="0 0 30 30" aria-hidden="true"><circle cx="15" cy="15" r="15" fill="#111"/><g fill="none" stroke="#fff" stroke-width="1.5"><circle cx="15" cy="15" r="8"/><ellipse cx="15" cy="15" rx="3.5" ry="8"/><path d="M7 15h16M8.5 11h13M8.5 19h13"/></g></svg>
      <span>www.tkvitality.com</span>
    </li>
  </ul>

  <div class="brand"><span class="brand__dot"></span>TK Vitality</div>

  <svg class="edge-band" viewBox="0 0 720 30" preserveAspectRatio="none" aria-hidden="true">
    <rect x="0" y="14" width="720" height="16" fill="var(--leaf)"/>
    <polygon points="440,14 720,0 720,14" fill="var(--orange)"/>
  </svg>
</section>

<section class="card card--back" aria-label="Card back">
  <div class="brand"><span class="brand__dot"></span>TK Vitality</div>
  <p class="back-url">www.tkvitality.com/my/username</p>
</section>

</body>
</html>
```